OPV Brantmoor Freight Limited

We need the buissnes card to be very exclusive. As we are all young in our company. We need this to be the gate to make our clients feel deep interest for us.

We are focused in as International Trade advisors, and our products go from Oil Tanker Ships to Rubber balls for dogs.

Our Slogan is Bringing Trade Home.
And our main marketing will be through Internet.

We were stablished in 2009 In Mexico and we also have offices in Hong Kong.
We have representatives in China and Europe.

Target Market(s)

Is every company or Individual that wants to develop an International Project or product development or Logistic service of Goods and people.
Some of our current projects are Ship Brokerage, Mine Brokerage, Real State and Product Pormotional development.

Industry/Entity Type

It Company

Requirements
Must have
• Our Logo and slogan, and make the card accoriding to the logo.
Nice to have
• Our Colors

```html
<!DOCTYPE html>
<html lang="en">
<head>
<meta charset="utf-8">
<title>OPV Brantmoor Freight Limited – Business Card</title>
<link href="https://fonts.googleapis.com/css2?family=Questrial&display=swap" rel="stylesheet">
<style>
  :root {
    --stage: #2a1d15;
    --card: #050505;
    --card-edge: #1a1a1a;
    --brand-green: #8dc63f;
    --brand-blue: #1e9ad6;
    --text-light: #e6e6e6;
    --text-muted: #a9a9a9;
  }
  * { margin: 0; padding: 0; box-sizing: border-box; }
  html, body {
    width: 1200px;
    height: 900px;
    overflow: hidden;
    background: var(--stage);
    font-family: "Questrial", "Helvetica Neue", Arial, sans-serif;
  }
  .canvas {
    position: relative;
    width: 1200px;
    height: 900px;
  }
  .card {
    position: absolute;
    width: 540px;
    height: 310px;
    background: radial-gradient(ellipse at 70% 30%, #151515 0%, var(--card) 65%);
    border: 1px solid var(--card-edge);
    border-radius: 22px;
    box-shadow: 0 14px 30px rgba(0, 0, 0, 0.55);
  }
  .card--front { left: 90px; top: 110px; }
  .card--back  { left: 570px; top: 480px; }

  .brand {
    position: absolute;
    display: flex;
    flex-direction: column;
    align-items: flex-start;
  }
  .brand__mark {
    display: flex;
    align-items: center;
    gap: 12px;
  }
  .brand__dot {
    width: 26px;
    height: 26px;
    border-radius: 50%;
    background: var(--brand-blue);
  }
  .brand__name {
    color: var(--brand-green);
    font-size: 64px;
    line-height: 1;
    letter-spacing: 6px;
  }
  .brand__slogan {
    margin-top: 6px;
    color: var(--brand-blue);
    font-size: 15px;
    letter-spacing: 0.5px;
  }
  .card--front .brand { left: 185px; top: 105px; }
  .card--back .brand  { left: 110px; top: 110px; }
  .card--back .brand__name { font-size: 52px; }
  .card--back .brand__slogan { font-size: 13px; }

  .divider {
    position: absolute;
    left: 300px;
    top: 92px;
    width: 3px;
    height: 96px;
    background: linear-gradient(to bottom, var(--brand-blue), var(--brand-green));
  }
  .contact {
    position: absolute;
    left: 318px;
    top: 88px;
    color: var(--text-light);
  }
  .contact__name { font-size: 17px; }
  .contact__role {
    font-size: 10px;
    color: var(--text-muted);
    margin-bottom: 14px;
  }
  .contact__line {
    font-size: 10.5px;
    line-height: 15px;
    color: var(--text-light);
    white-space: nowrap;
  }
  .contact__label { color: var(--text-muted); margin-right: 3px; }
</style>
</head>
<body>
  <main class="canvas">
    <section class="card card--front" aria-label="Card front">
      <div class="brand">
        <div class="brand__mark">
          <span class="brand__dot"></span>
          <span class="brand__name">OPV</span>
        </div>
        <span class="brand__slogan">Bringing Trade Home</span>
      </div>
    </section>

    <section class="card card--back" aria-label="Card back">
      <div class="brand">
        <div class="brand__mark">
          <span class="brand__dot"></span>
          <span class="brand__name">OPV</span>
        </div>
        <span class="brand__slogan">Bringing Trade Home</span>
      </div>
      <span class="divider"></span>
      <div class="contact">
        <p class="contact__name">Daniel Reyes</p>
        <p class="contact__role">general manager</p>
        <p class="contact__line"><span class="contact__label">p:</span>000 1111 2222 3333</p>
        <p class="contact__line"><span class="contact__label">m:</span>000 1111 2222 3333</p>
        <p class="contact__line"><span class="contact__label">e:</span>reyes@brantmoorfreight.com</p>
        <p class="contact__line"><span class="contact__label">w:</span>www.brantmoorfreight.com</p>
      </div>
    </section>
  </main>
</body>
</html>
```